Quarrybend Building Company / Website*

We need a design for a contracting company website based in KSA, something modern with the same color theme as the attached logo. including a page for people who want to submit their CV and try to apply for a job.Also to include the "about us, contact us, gallery, Divisions, Supplies, etc...". If possible to have an interactive or moving background. Please disregard the "Smart Solutions" Section in the attached profile.

Industry/Entity Type

Construction Company

Number of Pages Required

5+ page

Colors

Designer to choose colors to be used in the design.

Requirements
Must have
• Pages:
• about us, contact us, gallery, Divisions, Apply for a job, Supplies
Nice to have
• - Moving or interactive background

```html
<!DOCTYPE html>
<html lang="en">
<head>
<meta charset="utf-8">
<title>Quarrybend Building Company – Gallery</title>
<link rel="stylesheet" href="https://fonts.googleapis.com/css2?family=Rubik:wght@500;600&family=Lato:wght@400&display=swap">
<style>
  :root {
    --orange: #f4a020;
    --ink: #231a14;
    --footer: #140e0b;
    --white: #ffffff;
    --muted: #c9c2bd;
  }
  html, body { margin: 0; padding: 0; overflow: hidden; }
  body { width: 910px; height: 1200px; position: relative; background: var(--white); font-family: 'Lato', sans-serif; color: var(--ink); }
  .abs { position: absolute; }

  /* header */
  .call-bar { left: 538px; top: 0; width: 372px; height: 38px; }
  .call-text { left: 584px; top: 11px; font: 600 14px 'Rubik', sans-serif; color: var(--white); letter-spacing: .2px; white-space: nowrap; }
  .brand { left: 105px; top: 28px; font: 600 21px/1 'Rubik', sans-serif; color: var(--ink); }
  .brand small { display: block; font-size: 9.2px; margin-top: 4px; letter-spacing: .3px; }
  .brand-mark { left: 105px; top: 20px; width: 8px; height: 8px; background: var(--orange); }
  .nav a { position: absolute; top: 62px; font: 500 11.5px 'Rubik', sans-serif; color: var(--ink); text-decoration: none; white-space: nowrap; }
  .nav a.current { color: var(--orange); }
  .nav-underline { left: 467px; top: 80px; width: 50px; height: 2px; background: var(--ink); }

  /* hero */
  .hero { left: 0; top: 102px; width: 910px; height: 325px; }
  .hero-title { left: 0; top: 230px; width: 890px; text-align: center; font: 600 34px 'Rubik', sans-serif; color: var(--white); }

  /* gallery */
  .section-title { left: 0; top: 460px; width: 926px; text-align: center; font: 600 25px 'Rubik', sans-serif; color: var(--ink); margin: 0; }
  .tile { position: absolute; }
  .t-sky1 { background: linear-gradient(160deg, #2f6fb8, #6a5a3e); }
  .t-sky2 { background: linear-gradient(180deg, #4d7fbf, #9cc4dd 70%, #7a9fb8); }
  .t-sky3 { background: linear-gradient(180deg, #7fa4cf, #9c907a); }
  .t-sky4 { background: linear-gradient(180deg, #3f7cc4, #4e6f8f 60%, #b8ab93); }
  .t-sky5 { background: linear-gradient(180deg, #a9b6c8, #27466e); }
  .t-sky6 { background: linear-gradient(180deg, #cfd7df, #2a3a52); }

  /* footer */
  .footer { left: 0; top: 892px; width: 910px; height: 308px; background: var(--footer); }
  .footer-brand { left: 132px; top: 1040px; font: 600 17px/1 'Rubik', sans-serif; color: var(--white); }
  .footer-brand small { display: block; font-size: 6.6px; margin-top: 3px; letter-spacing: .3px; }
  .f-head { top: 947px; font: 500 12.5px 'Rubik', sans-serif; color: var(--white); margin: 0; white-space: nowrap; }
  .f-item { font-size: 11px; color: var(--white); white-space: nowrap; }
  .social-dot { width: 22px; height: 22px; border-radius: 50%; background: var(--white); }
  .divider { left: 0; top: 1137px; width: 910px; height: 1px; background: #2e2622; }
  .copyright { left: 0; top: 1153px; width: 868px; text-align: center; font-size: 11.5px; color: var(--muted); }
</style>
</head>
<body>

<header>
  <svg class="abs call-bar" viewBox="0 0 372 38" aria-hidden="true"><polygon points="0,0 372,0 372,38 44,38" fill="var(--orange)"/></svg>
  <div class="abs call-text">
    <svg width="12" height="12" viewBox="0 0 24 24" style="vertical-align:-1px;margin-right:3px" aria-hidden="true"><path d="M6.6 10.8a15 15 0 0 0 6.6 6.6l2.2-2.2c.3-.3.7-.4 1-.2 1.1.4 2.3.6 3.6.6.6 0 1 .4 1 1V20c0 .6-.4 1-1 1A17 17 0 0 1 3 4c0-.6.4-1 1-1h3.5c.6 0 1 .4 1 1 0 1.3.2 2.5.6 3.6.1.3 0 .7-.2 1z" fill="#fff"/></svg>CALL US NOW 600 555 0187
  </div>
  <div class="abs brand-mark"></div>
  <div class="abs brand">QUARRYBEND<small>BUILDING COMPANY</small></div>
  <nav class="nav">
    <a href="#" style="left:320px">HOME</a>
    <a href="#" style="left:381px">ABOUT US</a>
    <a href="#" class="current" style="left:466px">GALLERY</a>
    <a href="#" style="left:545px">DEPARTMENTS</a>
    <a href="#" style="left:657px">SUPPLIES</a>
    <a href="#" style="left:740px">CONTACT US</a>
  </nav>
  <div class="abs nav-underline"></div>
</header>

<section>
  <svg class="abs hero" viewBox="0 0 910 325" role="img" aria-label="Aerial view of a city skyline with towers and a construction crane">
    <defs>
      <linearGradient id="heroSky" x1="0" y1="0" x2="0" y2="1">
        <stop offset="0" stop-color="#6d6b69"/>
        <stop offset="0.4" stop-color="#8f7a62"/>
        <stop offset="1" stop-color="#7a6a55"/>
      </linearGradient>
    </defs>
    <rect width="910" height="325" fill="url(#heroSky)"/>
    <polygon points="0,318 258,318 453,249 646,318 910,318 910,325 0,325" fill="var(--orange)"/>
    <polygon points="275,325 453,263 631,325" fill="#fff"/>
  </svg>
  <h1 class="abs hero-title" style="margin:0">GALLERY</h1>
</section>

<main>
  <h2 class="abs section-title">OUR GALLERY</h2>
  <div class="tile t-sky1" style="left:110px;top:518px;width:165px;height:130px" role="img" aria-label="Building frame under construction with scaffolding"></div>
  <div class="tile t-sky2" style="left:282px;top:518px;width:165px;height:268px" role="img" aria-label="Tall glass tower with an arched top against a blue sky"></div>
  <div class="tile t-sky3" style="left:453px;top:518px;width:165px;height:130px" role="img" aria-label="Concrete towers rising with tower cranes"></div>
  <div class="tile t-sky4" style="left:627px;top:518px;width:165px;height:268px" role="img" aria-label="Modern office blocks under construction beside a road"></div>
  <div class="tile t-sky5" style="left:110px;top:657px;width:165px;height:129px" role="img" aria-label="Dark glass skyscraper next to a building under construction"></div>
  <div class="tile t-sky6" style="left:453px;top:657px;width:165px;height:129px" role="img" aria-label="Angular glass tower framed by palm trees"></div>
</main>

<footer>
  <div class="abs footer"></div>
  <div class="abs footer-brand">QUARRYBEND<small>BUILDING COMPANY</small></div>

  <h3 class="abs f-head" style="left:332px">CONTACT US</h3>
  <svg class="abs" style="left:334px;top:980px" width="12" height="14" viewBox="0 0 12 14" aria-hidden="true"><path d="M6 13s4.5-4.5 4.5-7.5a4.5 4.5 0 0 0-9 0C1.5 8.5 6 13 6 13z" fill="none" stroke="#fff"/><circle cx="6" cy="5.5" r="1.6" fill="none" stroke="#fff"/></svg>
  <div class="abs f-item" style="left:354px;top:980px">P.O.Box.4120 Harbor City 30417</div>
  <svg class="abs" style="left:334px;top:1007px" width="13" height="13" viewBox="0 0 24 24" aria-hidden="true"><path d="M6.6 10.8a15 15 0 0 0 6.6 6.6l2.2-2.2c.3-.3.7-.4 1-.2 1.1.4 2.3.6 3.6.6.6 0 1 .4 1 1V20c0 .6-.4 1-1 1A17 17 0 0 1 3 4c0-.6.4-1 1-1h3.5c.6 0 1 .4 1 1 0 1.3.2 2.5.6 3.6.1.3 0 .7-.2 1z" fill="none" stroke="#fff" stroke-width="1.5"/></svg>
  <div class="abs f-item" style="left:354px;top:1006px">+900 12 4410356</div>
  <svg class="abs" style="left:333px;top:1031px" width="14" height="14" viewBox="0 0 14 14" aria-hidden="true"><rect x="1" y="3" width="12" height="10" rx="1.5" fill="none" stroke="#fff"/><rect x="4" y="1" width="6" height="4" fill="none" stroke="#fff"/><path d="M4 8h1M7 8h1M10 8h0M4 10.5h1M7 10.5h1" stroke="#fff"/></svg>
  <div class="abs f-item" style="left:354px;top:1032px">+900 12 4410372</div>
  <svg class="abs" style="left:334px;top:1060px" width="13" height="10" viewBox="0 0 13 10" aria-hidden="true"><rect x="0.5" y="0.5" width="12" height="9" fill="none" stroke="#fff"/><path d="M0.5 0.5l6 5 6-5" fill="none" stroke="#fff"/></svg>
  <div class="abs f-item" style="left:354px;top:1058px">info@quarrybend.example</div>

  <h3 class="abs f-head" style="left:553px">COMPANY</h3>
  <div class="abs f-item" style="left:556px;top:981px">About us</div>
  <div class="abs f-item" style="left:556px;top:1003px">Gallery</div>
  <div class="abs f-item" style="left:556px;top:1024px">Divisions</div>
  <div class="abs f-item" style="left:556px;top:1046px">Supplies</div>
  <div class="abs f-item" style="left:556px;top:1068px">Contact us</div>

  <h3 class="abs f-head" style="left:680px">GET IN TOUCH</h3>
  <div class="abs social-dot" style="left:680px;top:978px"></div>
  <div class="abs f-item" style="left:708px;top:981px">Chirpline</div>
  <div class="abs social-dot" style="left:680px;top:1004px"></div>
  <div class="abs f-item" style="left:708px;top:1007px">Facetome</div>
  <div class="abs social-dot" style="left:680px;top:1030px"></div>
  <div class="abs f-item" style="left:708px;top:1033px">Linkwork</div>
  <div class="abs social-dot" style="left:680px;top:1056px"></div>
  <div class="abs f-item" style="left:708px;top:1059px">Snapgram</div>

  <div class="abs divider"></div>
  <div class="abs copyright">Copyright © 2019 All right reserved</div>
</footer>

</body>
</html>
```